Corporate Design für Garten- und Landschaftsbau
Sehr guter Desinger, sehr schnelle Reaktion auf Änderungswünsche, alles bestens gelaufen, jederzeit gerne wieder, vorbildlich.
Zielgruppe
-Garten- und Landschaftsbau
-Bagger- und Erdarbeiten
-Kellertrockenlegung
-Hausmeisterdienste
-Individuelle Gartengestaltung
Aufgabenstellung
Eventuell ein Baggerarm mit Baggerlöffel und oder einen Baum oder ein Strauch

```html
<!DOCTYPE html>
<html lang="de">
<head>
<meta charset="utf-8">
<title>Gartenbau Walt – Geschäftsausstattung</title>
<link href="https://fonts.googleapis.com/css2?family=Open+Sans:wght@400;600&family=Ubuntu:wght@400;500&display=swap" rel="stylesheet">
<style>
:root{
  --bg:#8d8d8d;
  --paper:#f4f4f2;
  --green:#5a7264;
  --green-text:#4d6a5a;
  --ink:#1f1f1f;
  --body:#3a3a3a;
  --muted:#6c7a72;
  --white:#ffffff;
}
*{margin:0;padding:0;box-sizing:border-box}
html,body{width:1200px;height:717px;overflow:hidden;background:var(--bg)}
.canvas{position:relative;width:1200px;height:717px}

/* Letterhead */
.letterhead{position:absolute;left:256px;top:48px;width:416px;height:588px;background:var(--paper);font-family:"Open Sans",sans-serif;overflow:hidden}
.brand{position:absolute;display:flex;align-items:center;gap:6px;font-family:"Ubuntu",sans-serif;font-weight:500;color:var(--green-text)}
.letterhead .brand{right:30px;top:34px;font-size:15px}
.brand-dot{width:10px;height:10px;border-radius:50%;background:var(--green)}
.letter-title{position:absolute;left:41px;top:198px;font-size:11px;font-weight:600;color:var(--ink)}
.letter-body{position:absolute;left:41px;top:226px;width:336px;font-size:5.6px;line-height:15.5px;color:var(--body)}
.letter-body p{margin-bottom:15.5px}
.closing{position:absolute;left:41px;top:428px;font-size:5.6px;color:var(--body)}
.fold-mark{position:absolute;left:0;width:14px;height:1px;background:#d9d6c6}
.letter-band{position:absolute;left:0;bottom:0;width:416px;height:60px}
.letter-footer{position:absolute;bottom:16px;font-size:3.6px;line-height:6.6px;color:var(--white)}
.letter-footer.left{left:38px}
.letter-footer.right{left:166px}

/* Business cards */
.card{position:absolute;left:706px;width:169px;height:106px;background:var(--paper);font-family:"Ubuntu",sans-serif;overflow:hidden}
.card-front{top:110px}
.card-back{top:243px}
.card .brand{left:20px;top:36px;font-size:14px}
.card-band{position:absolute;left:0;bottom:0;width:169px;height:26px}
.card-name{position:absolute;left:48px;bottom:6px;color:var(--white);line-height:1.1}
.card-name strong{display:block;font-size:6.8px;font-weight:500}
.card-name span{font-size:4.8px}
.contact{position:absolute;left:24px;top:14px;display:grid;grid-template-columns:33px 1fr;row-gap:3px;font-size:4.4px;line-height:5.4px}
.contact dt{color:var(--muted);text-transform:uppercase}
.contact dd{color:var(--green-text)}
.card-services{position:absolute;left:24px;bottom:10px;font-size:3.9px;line-height:5.6px;color:var(--white)}
</style>
</head>
<body>
<main class="canvas">

  <article class="letterhead">
    <div class="brand"><span class="brand-dot"></span>Gartenbau Walt</div>

    <span class="fold-mark" style="top:207px"></span>
    <span class="fold-mark" style="top:292px"></span>

    <h1 class="letter-title">Donec sodales sagittis magna.</h1>
    <div class="letter-body">
      <p>Lorem ipsum dolor sit amet, consectetuer adipiscing elit. Aenean commodo ligula eget dolor. Aenean massa. Cum sociis natoque penatibus et magnis dis parturient montes, nascetur ridiculus mus. Donec quam felis, ultricies nec, pellentesque eu, pretium quis, sem. Nulla consequat massa quis enim. Donec pede justo, fringilla vel, aliquet nec, vulputate eget, arcu. In enim justo, rhoncus ut, imperdiet a, venenatis vitae, justo.</p>
      <p>Nullam dictum felis eu pede mollis pretium. Integer tincidunt. Cras dapibus. Vivamus elementum semper nisi. Aenean vulputate eleifend tellus. Aenean leo ligula, porttitor eu, consequat vitae, eleifend ac, enim. Aliquam lorem ante, dapibus in, viverra quis, feugiat a, tellus. Phasellus viverra nulla ut metus varius laoreet. Quisque rutrum. Aenean imperdiet. Etiam ultricies nisi vel augue. Curabitur ullamcorper ultricies nisi. Nam eget dui. Etiam rhoncus. Maecenas tempus, tellus eget condimentum rhoncus, sem quam semper libero, sit amet adipiscing sem neque sed ipsum. Nam quam nunc, blandit vel, luctus pulvinar, hendrerit id, lorem. Maecenas nec odio et ante tincidunt tempus.</p>
    </div>
    <p class="closing">Mit freundlichen Grüßen</p>

    <svg class="letter-band" viewBox="0 0 416 60" preserveAspectRatio="none" aria-hidden="true">
      <path d="M0 20 Q208 -6 416 20 L416 60 L0 60 Z" fill="var(--green)"/>
    </svg>
    <div class="letter-footer left">
      Garten- und Landschaftsbau Walt<br>
      Geschäftsführer Jorben Mustermann<br>
      Lindenweg 4 | 55612 Tannhofen
    </div>
    <div class="letter-footer right">
      Tel.: 0170 1234567 | info@garten-landschaftsbau-walt.de | www.garten-landschaftsbau-walt.de<br>
      Bank Musterstadt | IBAN DE00 1234 5678 9000 1234 56 | BIC MUSTDEXX | Steuer-Nr. 01234/56789<br>
      Garten- und Landschaftspflege | Bagger- und Erdarbeiten | Kellertrockenlegung | Hausmeisterdienste
    </div>
  </article>

  <section class="card card-front">
    <div class="brand"><span class="brand-dot"></span>Gartenbau Walt</div>
    <svg class="card-band" viewBox="0 0 169 26" preserveAspectRatio="none" aria-hidden="true">
      <path d="M0 8 Q84 -4 169 8 L169 26 L0 26 Z" fill="var(--green)"/>
    </svg>
    <div class="card-name"><strong>Jorben Mustermann</strong><span>Geschäftsführer</span></div>
  </section>

  <section class="card card-back">
    <dl class="contact">
      <dt>Adresse</dt><dd>Lindenweg 4<br>55612 Tannhofen</dd>
      <dt>Telefon</dt><dd>Tel.: 0170 1234567</dd>
      <dt>Email<br>Internet</dt><dd>info@garten-landschaftsbau-walt.de<br>www.garten-landschaftsbau-walt.de</dd>
    </dl>
    <svg class="card-band" style="height:36px" viewBox="0 0 169 36" preserveAspectRatio="none" aria-hidden="true">
      <path d="M0 10 Q84 -5 169 10 L169 36 L0 36 Z" fill="var(--green)"/>
    </svg>
    <div class="card-services">
      Garten- und Landschaftspflege | Bagger- und Erdarbeiten<br>
      Kellertrockenlegung | Hausmeisterdienste
    </div>
  </section>

</main>
</body>
</html>
```